Print Ad Design

I need an ad designed to promote an event that we are hosting at a trade show for placement in the show program. The art must be ready to submit to the publication by Friday, November 15th at the latest. The ad is 1/2 page in the show program that will be 4.25"X 5.5" and must be submitted as a high resolution (300dpi) PDF. Ad is full colour. The minimum bleed and trim marks are 0.25". The trade show is the Northern Herd Fair in Canada and we would like to promote a 2 day training we will be hosting at the close of the show. Our company is PastureWise Partners - Ultrasound and Diagnostics and the details that should be included in the ad are:
YOU CAN USE ULTRASOUND TO MANAGE YOUR PREG CHECKS
On Farm Ultrasound Training for Producers
When - Friday, Feb. 7th & Saturday, Feb. 8th
9 AM - 5 PM
Where - close to Herd FAIR
Lunch provided
Registration $175 per day - $300 total
Introduction to ultrasound
Reproductive system anatomy
Pregnancy diagnosis
Live on farm scanning demonstrations and practice with case discussions
Tuition redeemable towards the purchase of ultrasound system.
TO REGISTER OR LEARN MORE
email - info@pasturewisepartners.ca or call 1-800-431-5067
(I have attached our logo and some possible images to use in the ad)
Please note that the primary logo to feature is PastureWise Partners and the secondary logo to use in the ad is Veloskar Ultrasound Scanners.
THANK YOU!!!
Target Market(s)
Dairy Farmers (men and women)
Industry/Entity Type
Trade

```html
<!DOCTYPE html>
<html lang="en">
<head>
<meta charset="utf-8">
<title>On Farm Ultrasound Training – PastureWise Partners</title>
<link href="https://fonts.googleapis.com/css2?family=Roboto+Condensed:wght@400;500;700&family=Roboto:wght@400&display=swap" rel="stylesheet">
<style>
:root{
  --stage:#3a3a3a;
  --rule:#8a8a8a;
  --navy:#1b5786;
  --navy-dark:#16466f;
  --gold:#fcc50d;
  --white:#ffffff;
  --ink:#1b4f80;
}
*{margin:0;padding:0;box-sizing:border-box}
html,body{width:1200px;height:1000px;overflow:hidden;background:var(--stage)}
body{position:relative;font-family:"Roboto Condensed",Arial,sans-serif}
.dim{position:absolute;color:#9a9a9a;font:500 15px "Roboto",Arial,sans-serif}
.dim-line{position:absolute;background:var(--rule)}
.ad{position:absolute;left:271px;top:97px;width:657px;height:850px;background:var(--navy);overflow:hidden;box-shadow:3px 4px 8px rgba(0,0,0,.45)}
.header{position:absolute;left:0;top:0;width:421px;height:98px;background:var(--white)}
.headline{position:absolute;left:16px;top:27px;color:var(--ink);font-size:29px;line-height:25px;font-weight:400;letter-spacing:-.2px;white-space:nowrap}
.headline strong{font-weight:700}
.header-rule{position:absolute;left:0;top:92px;width:421px;height:4px;background:linear-gradient(90deg,var(--gold) 30%,rgba(252,197,13,.2))}
.accent-bar{position:absolute;left:0;top:133px;width:44px;height:225px;background:var(--gold)}
.details{position:absolute;left:55px;top:132px;color:var(--white);text-transform:uppercase}
.details h2{font-size:24px;line-height:26px;font-weight:700;margin-bottom:10px}
.details .label{color:var(--gold);font-size:17px;font-weight:700;line-height:19px}
.details p{font-size:17px;line-height:19px;font-weight:500}
.details .group{margin-bottom:16px}
.topics{position:absolute;left:0;top:381px;width:421px;height:154px;background:linear-gradient(90deg,#fff 55%,#c9d8e6 78%,var(--navy) 100%);padding:12px 0 0 57px}
.topics li{list-style:none;font-size:20px;line-height:27px;color:var(--ink)}
.topics li.hi{color:var(--gold)}
.tuition{position:absolute;left:58px;top:571px;color:var(--white);font-size:24px;line-height:26px;font-weight:500}
.tuition-rule{position:absolute;left:54px;top:647px;width:367px;height:3px;background:linear-gradient(90deg,var(--gold) 60%,rgba(252,197,13,0))}
.register{position:absolute;left:55px;top:672px;color:var(--white)}
.register h3{color:var(--gold);font-size:29px;line-height:28px;font-weight:700}
.register .sub{font-size:15px;line-height:16px;margin-bottom:10px}
.register .contact{font-size:20px;line-height:23px;font-weight:500}
.partner{position:absolute;left:55px;top:784px;color:var(--gold);font-size:14px;font-weight:700;letter-spacing:.5px;line-height:16px}
.photo{position:absolute;left:421px;width:236px}
.photo-top{top:0;height:283px;background:linear-gradient(160deg,#2c3d5c 0%,#8f8f86 45%,#d9d7cf 70%,#6b5f4a 100%)}
.photo-bottom{top:283px;height:400px;background:linear-gradient(120deg,#c9c4b6 0%,#bfcfcc 30%,#7fc7bb 50%,#2a2a2a 75%,#e8e3da 100%)}
.corner{position:absolute;left:0;top:0}
.brand{position:absolute;left:350px;top:738px;color:var(--ink);display:flex;align-items:center;gap:12px}
.brand .mark{width:62px;height:62px;border-radius:50%;background:var(--gold)}
.brand .name{font-size:30px;line-height:30px;font-weight:500}
.brand .name small{display:block;font-size:16px;line-height:20px;font-weight:500}
</style>
</head>
<body>
  <div class="dim-line" style="left:181px;top:46px;width:358px;height:1px"></div>
  <div class="dim" style="left:555px;top:37px">4.25"</div>
  <div class="dim-line" style="left:622px;top:46px;width:358px;height:1px"></div>
  <div class="dim-line" style="left:182px;top:260px;width:1px;height:255px"></div>
  <div class="dim" style="left:167px;top:530px">5.5"</div>
  <div class="dim-line" style="left:182px;top:570px;width:1px;height:255px"></div>

  <div class="ad">
    <div class="header">
      <h1 class="headline">YOU CAN USE <strong>ULTRASOUND</strong><br><strong>TO MANAGE YOUR PREG CHECKS</strong></h1>
      <div class="header-rule"></div>
    </div>

    <div class="accent-bar"></div>
    <div class="details">
      <h2>On Farm Ultrasound Training<br>for Producers</h2>
      <div class="group">
        <div class="label">When</div>
        <p>Friday, Feb. 7<sup style="font-size:10px">th</sup> &amp; Saturday, Feb. 8<sup style="font-size:10px">th</sup><br>9 AM - 5 PM</p>
      </div>
      <div class="group">
        <div class="label">Where</div>
        <p>Close to Herd FAIR</p>
      </div>
      <div class="group">
        <div class="label">Lunch Provided</div>
        <p>Registration $175 per day - $300 total</p>
      </div>
    </div>

    <ul class="topics">
      <li class="hi">Introduction to ultrasound</li>
      <li>Reproductive system anatomy</li>
      <li class="hi">Pregnancy diagnosis</li>
      <li>Live on farm scanning demonstrations</li>
      <li>and practice with case discussions</li>
    </ul>

    <p class="tuition">Tuition redeemable towards<br>the purchase of ultrasound system.</p>
    <div class="tuition-rule"></div>

    <div class="register">
      <h3>TO REGISTER</h3>
      <p class="sub">OR LEARN MORE</p>
      <p class="contact">info@pasturewisepartners.ca<br>1.800.431.5067</p>
    </div>
    <div class="partner">VELOSKAR<br>ULTRASOUND SCANNERS</div>

    <div class="photo photo-top" role="img" aria-label="Photo: two producers in aprons using handheld ultrasound scanners on a cow"></div>
    <div class="photo photo-bottom" role="img" aria-label="Photo: a technician in a green gown scanning a Holstein cow with a portable ultrasound unit"></div>

    <svg class="corner" width="657" height="850" viewBox="0 0 657 850" aria-hidden="true">
      <path d="M262 850 C 290 715, 490 645, 657 650 L657 850 Z" fill="var(--gold)"/>
      <path d="M276 850 C 305 728, 500 660, 657 664 L657 850 Z" fill="var(--white)"/>
    </svg>

    <div class="brand">
      <div class="mark"></div>
      <div class="name">PastureWise Partners<small>ultrasound and diagnostics</small></div>
    </div>
  </div>
</body>
</html>
```